Need Professional, Modern, Clean Newsletter Templates for High End Real Estate Agents in Orange Coun

I need a newsletter for realtors who specialize in high-end home sales for Orange County, California. Please see the attached draft of the newsletter we have in mind. Please note the logo at the top and the beach imagery and please use these and complementary fonts, colors and themes when creating your design. These particular realtors focus on very high-end clients with a specialization on ocean front properties. I WANT YOU TO PLEASE USE THE HEADER FROM MY ATTACHMENT IN YOUR NEWSLETTER. THIS NEWSLETTER IS INTENDED TO BE SENT OUT VIA EMAIL ONLY, NOT PRINT.

The idea behind the newsletter is that it will cover four broad categories. We will have a content creator who will pull content each week, however we need a nice looking template that can support their content. These are the four categories :

1) Market Data - this will pull graphs and information that the realtors receive, directly from the MLS (home listing site). Most of this will be in graph or table form, so we need a nice way to support that.

2.) Featured Listings - this will show the featured homes they have for sale at any given time. This section of the template should have a place to put pictures of the home with supporting text.

3.) News you can use - links to videos and articles relevant to the real estate industry and in the area.

4.) Upcoming OC Events - list of upcoming events in the area.
Updates

I feel like I need to post this update in case there was some confusion in my contest brief.

I DO NOT want a new logo or header design. What I am looking for is a newsletter to support the header and logo I already have, and for a nice template which includes each of the four sections I described in my brief. I would like you to think about each of the four sections and design them accordingly. There needs to be a good section for graphs (market data), for videos, for featured listings (pictures of homes with supporting descriptive text) and upcoming events (maybe supported by a calendar and text sections to describe the event, etc.)

This newsletter will be sent out as email only. Your entries should be made as .pdf or as a word document. Thanks.

Target Market(s)

High end real estate buyers and sellers, with a focus on ocean front property.

Industry/Entity Type

Real Estate

Colors
33a6d7
00a990
86cae6

Requirements
Must have
• You MUST include the header photo from the .png attachment I included. "Varnell at the Shore - Sell with the Best."

```html
<!DOCTYPE html>
<html lang="en">
<head>
<meta charset="utf-8">
<title>Varnell at the Shore – Newsletter</title>
<link rel="stylesheet" href="https://fonts.googleapis.com/css2?family=Lato:wght@400;700&family=Oswald:wght@300;400&display=swap">
<style>
:root{
  --backdrop:#0b3e72;
  --teal:#00a990;
  --blue:#33a6d7;
  --sky:#86cae6;
  --navy:#1c3f6e;
  --ink:#3b3b3b;
  --muted:#7d7d7d;
  --panel:#eceeef;
  --line:#d9dcde;
  --white:#ffffff;
}
*{box-sizing:border-box;margin:0;padding:0}
html,body{width:1200px;height:3629px;overflow:hidden}
body{background:var(--backdrop);font-family:"Lato",sans-serif;color:var(--ink);position:relative}
.email{position:absolute;left:200px;top:44px;width:800px;height:3500px;background:var(--white);box-shadow:0 18px 30px rgba(0,0,0,.35)}
.dateline{height:67px;text-align:right;padding:22px 22px 0;font-size:17px;color:#555}
.hero{height:320px;position:relative;background:linear-gradient(180deg,#7fb9dc 0%,#b6dcef 22%,#2aa3c6 40%,#2b9fc0 62%,#cfe5e3 78%,#d8c8a8 100%)}
.brand{position:absolute;left:36px;top:140px;display:flex;align-items:center;gap:14px;font-family:"Lato",sans-serif;font-weight:700;color:var(--white);font-size:30px;line-height:1}
.brand i{display:block;width:18px;height:18px;border-radius:50%;background:var(--white)}
.tagline{position:absolute;right:28px;top:136px;font-family:"Oswald",sans-serif;font-weight:300;font-size:38px;color:var(--white);letter-spacing:2px;text-transform:uppercase}
.nav{height:65px;background:var(--teal);display:flex;justify-content:space-around;align-items:center;padding:0 10px}
.nav a{color:var(--white);font-size:15px;font-weight:700;text-decoration:none;text-transform:uppercase;letter-spacing:.5px}
.intro{margin-top:58px;height:324px;background:var(--panel);display:flex}
.portrait{width:242px;height:324px;background:linear-gradient(160deg,#5a4a3c,#8c7a66 55%,#3d332b)}
.intro-text{padding:30px 30px 0 30px;flex:1}
.intro h1{font-size:28px;font-weight:700;color:var(--teal);letter-spacing:1px;text-transform:uppercase}
.intro p{margin-top:14px;font-size:16px;line-height:31px;color:#666}
.intro .agent{margin-top:26px;font-size:21px;font-weight:700;color:var(--ink);text-transform:uppercase;letter-spacing:1px}
.intro .mail{display:inline-block;margin-top:6px;font-size:17px;font-weight:700;color:var(--teal);text-decoration:underline}
.sections{margin:82px 16px 0;display:grid;grid-template-columns:1fr 1fr;row-gap:44px}
.topic{padding:0 24px;min-height:124px}
.topic:nth-child(odd){border-right:1px solid var(--line)}
.topic h2{display:flex;align-items:center;gap:18px;font-size:22px;font-weight:400;color:var(--ink)}
.num{width:46px;height:46px;border:2px solid var(--blue);border-radius:50%;display:flex;align-items:center;justify-content:center;color:var(--blue);font-size:22px}
.topic p{margin-top:20px;font-size:16px;line-height:30px;color:var(--muted)}
.market{margin-top:80px;width:800px;border-collapse:collapse;background:var(--panel)}
.market th{height:58px;background:var(--blue);color:var(--white);font-size:17px;font-weight:700}
.market td{text-align:center;font-size:15.5px;color:#555;height:44px;border-left:1px solid var(--line)}
.market td:first-child{text-align:left;padding-left:26px;border-left:0;width:216px}
.market tr.first td{padding-top:18px;height:62px}
.market tr.trend td{height:146px}
.trend-link{display:block;color:var(--teal);font-size:16px;margin-top:8px}
.band-head{margin-top:75px;height:56px;background:var(--blue);color:var(--white);font-size:15px;font-weight:700;padding:20px 26px;text-transform:uppercase;letter-spacing:.5px}
.featured{height:380px;background:var(--panel);display:flex;padding:30px 26px}
.listing{width:300px;font-size:16px;line-height:28px;color:#444}
.listing .price{font-size:27px;font-weight:700;color:var(--navy);margin:14px 0 10px}
.listing a{display:block;margin-top:20px;color:var(--navy);font-weight:700;text-decoration:underline}
.news{margin-top:90px;height:354px;background:var(--teal);text-align:center;padding-top:50px}
.news h2{font-family:"Oswald",sans-serif;font-weight:300;font-size:34px;color:var(--white);letter-spacing:1px}
.videos{margin-top:42px;display:flex;justify-content:center;gap:34px}
.video{width:210px;height:136px;background:#1c2a2f;border:6px solid #0f4a43;position:relative}
.video .screen{position:absolute;inset:0;background:linear-gradient(180deg,#3a4a58 0%,#6f8796 55%,#1b2227 100%)}
.events{padding:68px 40px 0}
.events h2{font-size:22px;font-weight:700;color:var(--navy);text-transform:uppercase;letter-spacing:.5px;padding-bottom:24px;border-bottom:2px solid var(--line)}
.event-list{display:flex;margin-top:44px}
.event{width:380px;display:flex;gap:14px}
.date{width:58px;height:64px;background:var(--teal);color:var(--white);text-align:center;line-height:1;padding-top:6px}
.date b{display:block;font-size:28px}
.date span{font-size:16px;text-transform:uppercase}
.event h3{font-size:21px;font-weight:400;color:var(--ink);text-transform:uppercase}
.event .meta{display:flex;gap:10px;font-size:15.5px;line-height:30px;color:#999;margin-top:6px}
.event .meta svg{flex:none;margin-top:8px}
.event a{display:block;margin-top:14px;color:var(--teal);font-weight:700;font-size:17px;text-decoration:none;padding-left:10px}
.touch{position:absolute;left:0;top:3167px;width:800px;height:95px;background:#e5e5e5;display:flex;align-items:center;justify-content:space-between;padding:0 28px}
.touch h2{font-size:24px;font-weight:400;color:#555;letter-spacing:1px}
.social{display:flex;gap:26px}
.social span{width:42px;height:42px;background:var(--blue);display:block}
.footer{position:absolute;left:0;top:3262px;width:800px;text-align:center;padding-top:52px;font-size:15px;line-height:32px;color:#777}
.footer a{color:var(--blue);text-decoration:none}
</style>
</head>
<body>
<main class="email">
  <div class="dateline">Fri, Feb 21, 2014 at 6:52 AM</div>

  <header class="hero" role="img" aria-label="Ocean shoreline with blue water and sandy beach">
    <div class="brand"><i></i>Varnell at the Shore</div>
    <div class="tagline">Sell with the Best</div>
  </header>

  <nav class="nav">
    <a href="#">Market Data</a><a href="#">Featured Listings</a><a href="#">Real Estate News</a><a href="#">OC Events</a>
  </nav>

  <section class="intro">
    <div class="portrait" role="img" aria-label="Portrait photo of the agent"></div>
    <div class="intro-text">
      <h1>Jan 2014 Newsletter</h1>
      <p>Elementum pellentesque aliquet. Nullam sodales urna erat, vitae egestas nisl tincidunt et. Sed iaculis rhoncus dolor. Integer vel urna nec elit varius dapibus ac nec mi. Vestibulum at nulla nec nulla pharetra sollicitudin.</p>
      <div class="agent">Reed Halvorsen</div>
      <a class="mail" href="#">Email Me</a>
    </div>
  </section>

  <section class="sections">
    <div class="topic"><h2><span class="num">1</span>Real Estate Market Data</h2><p>Track monthly changes in property values and market trends</p></div>
    <div class="topic"><h2><span class="num">2</span>Featured Property Listings</h2><p>Some of the best properties presently available for sale in OC</p></div>
    <div class="topic"><h2><span class="num">3</span>News You Can Use</h2><p>Follow the latest news and issues impacting the real estate market</p></div>
    <div class="topic"><h2><span class="num">4</span>OC Community Events</h2><p>Upcoming events of note in the Orange County community</p></div>
  </section>

  <table class="market">
    <tr><th>Zip Code:</th><th>92677</th><th>92651</th><th>92672</th><th>92673</th><th>92629</th></tr>
    <tr class="first"><td>Monthly Units Sold</td><td>115</td><td>116</td><td>117</td><td>118</td><td>119</td></tr>
    <tr><td>Avg. Sold Price</td><td>$583K</td><td>$583K</td><td>$583K</td><td>$583K</td><td>$583K</td></tr>
    <tr><td>Sold % of Orig List $</td><td>95.5%</td><td>95.5%</td><td>95.5%</td><td>95.5%</td><td>95.5%</td></tr>
    <tr><td>Current Units Listed</td><td>122</td><td>122</td><td>122</td><td>122</td><td>122</td></tr>
    <tr><td>Avg. List Price</td><td>$1,415K</td><td>$1,415K</td><td>$1,415K</td><td>$1,415K</td><td>$1,415K</td></tr>
    <tr><td>Avg. Days on Market</td><td>83</td><td>83</td><td>83</td><td>83</td><td>83</td></tr>
    <tr class="trend"><td>Historical Trends</td>
      <td><svg width="40" height="40" viewBox="0 0 40 40"><circle cx="20" cy="20" r="17" fill="none" stroke="#00a990" stroke-width="3"/><rect x="12" y="19" width="3" height="9" fill="#00a990"/><rect x="18.5" y="13" width="3" height="15" fill="#00a990"/><rect x="25" y="16" width="3" height="12" fill="#00a990"/></svg><a class="trend-link" href="#">See Chart</a></td>
      <td><svg width="40" height="40" viewBox="0 0 40 40"><circle cx="20" cy="20" r="17" fill="none" stroke="#00a990" stroke-width="3"/><rect x="12" y="19" width="3" height="9" fill="#00a990"/><rect x="18.5" y="13" width="3" height="15" fill="#00a990"/><rect x="25" y="16" width="3" height="12" fill="#00a990"/></svg><a class="trend-link" href="#">See Chart</a></td>
      <td><svg width="40" height="40" viewBox="0 0 40 40"><circle cx="20" cy="20" r="17" fill="none" stroke="#00a990" stroke-width="3"/><rect x="12" y="19" width="3" height="9" fill="#00a990"/><rect x="18.5" y="13" width="3" height="15" fill="#00a990"/><rect x="25" y="16" width="3" height="12" fill="#00a990"/></svg><a class="trend-link" href="#">See Chart</a></td>
      <td><svg width="40" height="40" viewBox="0 0 40 40"><circle cx="20" cy="20" r="17" fill="none" stroke="#00a990" stroke-width="3"/><rect x="12" y="19" width="3" height="9" fill="#00a990"/><rect x="18.5" y="13" width="3" height="15" fill="#00a990"/><rect x="25" y="16" width="3" height="12" fill="#00a990"/></svg><a class="trend-link" href="#">See Chart</a></td>
      <td><svg width="40" height="40" viewBox="0 0 40 40"><circle cx="20" cy="20" r="17" fill="none" stroke="#00a990" stroke-width="3"/><rect x="12" y="19" width="3" height="9" fill="#00a990"/><rect x="18.5" y="13" width="3" height="15" fill="#00a990"/><rect x="25" y="16" width="3" height="12" fill="#00a990"/></svg><a class="trend-link" href="#">See Chart</a></td>
    </tr>
  </table>

  <div class="band-head">Featured Listings</div>
  <section class="featured">
    <div class="listing">
      18 Tidewater Lane<br>Seacliff Point, CA 92677
      <div class="price">$489,900</div>
      Bedrooms: 2 beds<br>Bathrooms: 2 full<br>Sq. Footage: 1,200<br>MLS# OC13245720
      <a href="#">View Listing Details</a>
    </div>
    <svg class="chart" width="440" height="230" viewBox="0 0 440 230" font-family="Lato, sans-serif">
      <g font-size="11" fill="#777" text-anchor="end">
        <text x="24" y="58">500</text><text x="24" y="83">400</text><text x="24" y="108">300</text>
        <text x="24" y="133">200</text><text x="24" y="158">100</text><text x="24" y="183">0</text>
      </g>
      <g fill="#d6dde2">
        <rect x="44" y="54" width="14" height="126"/><rect x="72" y="54" width="14" height="126"/><rect x="100" y="54" width="14" height="126"/><rect x="128" y="54" width="14" height="126"/><rect x="156" y="54" width="14" height="126"/><rect x="184" y="54" width="14" height="126"/><rect x="212" y="54" width="14" height="126"/><rect x="240" y="54" width="14" height="126"/><rect x="268" y="54" width="14" height="126"/><rect x="296" y="54" width="14" height="126"/><rect x="324" y="54" width="14" height="126"/><rect x="352" y="54" width="14" height="126"/><rect x="380" y="54" width="14" height="126"/><rect x="408" y="54" width="14" height="126"/>
      </g>
      <g fill="#3fb7b9">
        <rect x="44" y="164" width="14" height="16"/><rect x="72" y="108" width="14" height="72"/><rect x="100" y="96" width="14" height="84"/><rect x="128" y="76" width="14" height="104"/><rect x="156" y="126" width="14" height="54"/><rect x="184" y="110" width="14" height="70"/><rect x="212" y="140" width="14" height="40"/><rect x="240" y="164" width="14" height="16"/><rect x="268" y="86" width="14" height="94"/><rect x="296" y="72" width="14" height="108"/><rect x="324" y="98" width="14" height="82"/><rect x="352" y="116" width="14" height="64"/><rect x="380" y="136" width="14" height="44"/><rect x="408" y="154" width="14" height="26"/>
      </g>
      <g font-size="11" font-weight="700" fill="#555" text-anchor="middle">
        <text x="51" y="198">S</text><text x="79" y="198">M</text><text x="107" y="198">T</text><text x="135" y="198">W</text><text x="163" y="198">T</text><text x="191" y="198">F</text><text x="219" y="198">S</text><text x="247" y="198">S</text><text x="275" y="198">M</text><text x="303" y="198">T</text><text x="331" y="198">W</text><text x="359" y="198">T</text><text x="387" y="198">F</text><text x="415" y="198">S</text>
      </g>
      <rect x="40" y="6" width="212" height="48" rx="3" fill="#3a3f45"/>
      <path d="M128 54 L135 62 L142 54 Z" fill="#3a3f45"/>
      <text x="146" y="35" font-size="13" font-weight="700" fill="#fff" text-anchor="middle">Wednesday, December 3</text>
    </svg>
  </section>

  <section class="news">
    <h2>News You Can Use</h2>
    <div class="videos">
      <div class="video"><div class="screen" role="img" aria-label="Video still of a real estate news broadcast"></div>
        <svg style="position:absolute;left:82px;top:44px" width="36" height="36" viewBox="0 0 36 36"><circle cx="18" cy="18" r="16" fill="none" stroke="#fff" stroke-width="3"/><path d="M14 11 L26 18 L14 25 Z" fill="#fff"/></svg></div>
      <div class="video"><div class="screen" role="img" aria-label="Video still of a market report segment"></div></div>
      <div class="video"><div class="screen" role="img" aria-label="Video still of a housing trends segment"></div></div>
    </div>
  </section>

  <section class="events">
    <h2>Upcoming Events</h2>
    <div class="event-list">
      <div class="event">
        <div class="date"><b>25</b><span>Oct</span></div>
        <div>
          <h3>Lorem Ipsum Dolor</h3>
          <div class="meta"><svg width="12" height="16" viewBox="0 0 12 16"><path d="M6 0C2.7 0 0 2.6 0 5.9 0 10 6 16 6 16s6-6 6-10.1C12 2.6 9.3 0 6 0zm0 8a2 2 0 110-4 2 2 0 010 4z" fill="#aaa"/></svg><span>Harbor View Hall Lorem<br>Ipsum dummy text London<br>United Kingdom 0918</span></div>
          <div class="meta"><svg width="14" height="14" viewBox="0 0 14 14"><circle cx="7" cy="7" r="6" fill="none" stroke="#aaa" stroke-width="1.5"/><path d="M7 3.5V7h3" fill="none" stroke="#aaa" stroke-width="1.5"/></svg><span>12:30 Pm $ 25.00 / Person</span></div>
          <a href="#">View Details</a>
        </div>
      </div>
      <div class="event">
        <div class="date"><b>25</b><span>Dec</span></div>
        <div>
          <h3>Lorem Ipsum Dolor</h3>
          <div class="meta"><svg width="12" height="16" viewBox="0 0 12 16"><path d="M6 0C2.7 0 0 2.6 0 5.9 0 10 6 16 6 16s6-6 6-10.1C12 2.6 9.3 0 6 0zm0 8a2 2 0 110-4 2 2 0 010 4z" fill="#aaa"/></svg><span>Harbor View Hall Lorem<br>Ipsum dummy text London<br>United Kingdom 0918</span></div>
          <div class="meta"><svg width="14" height="14" viewBox="0 0 14 14"><circle cx="7" cy="7" r="6" fill="none" stroke="#aaa" stroke-width="1.5"/><path d="M7 3.5V7h3" fill="none" stroke="#aaa" stroke-width="1.5"/></svg><span>12:30 Pm $ 25.00 / Person</span></div>
          <a href="#">View Details</a>
        </div>
      </div>
    </div>
  </section>

  <section class="touch">
    <h2>Stay In Touch With Us:</h2>
    <div class="social"><span></span><span></span><span></span><span></span><span></span></div>
  </section>

  <footer class="footer">
    Copyright © 2014 VarnellattheShore, All rights reserved.<br>
    Our mailing address is: VarnellattheShore 14 Cove Harbor Lane Seacliff Point, CA 92629<br>
    <a href="#">unsubscribe from this list</a> | <a href="#">update subscription preferences</a>
  </footer>
</main>
</body>
</html>
```